a promotional poster design to promote our upcoming event. We want the date to be promoted as "Save the Date" for Sunday 4th July 2021.

Poster design

Requirements
Must have
• the following text;

Save the Date! (stand out)
Sunday 4th July 2021 (stand out)
KORB Family Mixed Netball Carnival
Nice to have
• make the date stand out. We want people to lock in the date we're promoting.

```html
<!DOCTYPE html>
<html lang="en">
<head>
<meta charset="utf-8">
<title>KORB Family Mixed Netball Carnival – Save the Date</title>
<link rel="stylesheet" href="https://fonts.googleapis.com/css2?family=Anton&family=Bangers&family=Roboto+Condensed:wght@700&family=Libre+Baskerville:ital@1&display=swap">
<style>
  :root{
    --page:#ffffff;
    --amber:#e6a22e;
    --amber-deep:#d98a1e;
    --floor:#c98a4e;
    --floor-dark:#8a5a34;
    --red:#c4302b;
    --red-deep:#8e1f1c;
    --orange:#ef7a22;
    --yellow:#f8bd16;
    --ink:#121212;
    --paper:#f7f7f5;
  }
  html,body{margin:0;padding:0;width:1200px;height:1181px;overflow:hidden;background:var(--page);}
  .poster{position:absolute;left:312px;top:218px;width:568px;height:758px;box-shadow:4px 4px 8px rgba(0,0,0,.25);}
  .poster svg{display:block;width:100%;height:100%;}
  .title{font-family:"Bangers",cursive;fill:var(--ink);font-size:42px;letter-spacing:.5px;}
  .headline{font-family:"Bangers",cursive;fill:var(--ink);}
  .date{font-family:"Anton",sans-serif;fill:var(--ink);font-size:74px;letter-spacing:3px;}
  .org-name{font-family:"Roboto Condensed",sans-serif;font-weight:700;fill:var(--ink);font-size:15px;}
  .org-tagline{font-family:"Libre Baskerville",serif;font-style:italic;fill:#fff;font-size:12px;}
  .program-name{font-family:"Bangers",cursive;fill:var(--orange);font-size:26px;}
</style>
</head>
<body>
<div class="poster">
  <svg viewBox="0 0 710 948" xmlns="http://www.w3.org/2000/svg">
    <defs>
      <linearGradient id="court" x1="0" y1="0" x2="0" y2="1">
        <stop offset="0" stop-color="var(--amber)"/>
        <stop offset=".35" stop-color="var(--amber-deep)"/>
        <stop offset=".7" stop-color="var(--floor)"/>
        <stop offset="1" stop-color="var(--floor-dark)"/>
      </linearGradient>
    </defs>

    <rect class="court-photo" role="img" aria-label="Photo of players in team uniforms on an indoor netball court" x="0" y="0" width="710" height="948" fill="url(#court)"/>

    <!-- top banner bands -->
    <polygon class="band-red" points="305,132 710,178 710,230 305,208" fill="var(--red)"/>
    <polygon class="band-orange" points="420,205 710,200 710,258 420,240" fill="var(--orange)"/>
    <polygon class="band-yellow" points="120,215 520,210 710,248 710,262 120,240" fill="var(--yellow)"/>

    <!-- main white panel -->
    <polygon class="panel" points="0,240 710,258 710,488 560,610 100,758 0,380" fill="var(--paper)"/>

    <!-- lower ribbon bands -->
    <polygon class="band-yellow" points="100,758 565,610 565,790 300,790" fill="var(--yellow)"/>
    <polygon class="band-orange" points="190,768 565,790 565,848 190,820" fill="var(--orange)"/>
    <polygon class="band-red" points="280,820 460,840 460,905 280,915" fill="var(--red)"/>
    <polygon class="band-red-deep" points="275,860 460,880 460,930 275,928" fill="var(--red-deep)"/>

    <!-- dashed frame -->
    <rect class="frame" x="25" y="25" width="660" height="895" fill="none" stroke="var(--ink)" stroke-width="2" stroke-dasharray="9 6"/>

    <!-- event title -->
    <text class="title" text-anchor="middle">
      <tspan x="175" y="88">KORB FAMILY</tspan>
      <tspan x="175" y="142">MIXED NETBALL</tspan>
      <tspan x="175" y="196">CARNIVAL</tspan>
    </text>

    <!-- organiser -->
    <circle class="org-mark" cx="572" cy="105" r="26" fill="var(--red)"/>
    <text class="org-name" text-anchor="middle">
      <tspan x="572" y="187">RIVERBEND COMMUNITY</tspan>
      <tspan x="572" y="205">HEALTH SERVICE</tspan>
    </text>
    <text class="org-tagline" x="572" y="223" text-anchor="middle">Caring for the Community</text>

    <!-- save the date -->
    <text class="headline" font-size="92" transform="translate(165,350) rotate(-16)">SAVE</text>
    <text class="headline" font-size="76" transform="translate(130,455) rotate(-16)">THE DATE!</text>
    <text class="headline" font-size="82" x="330" y="483">SUNDAY</text>

    <line class="rule" x1="130" y1="506" x2="580" y2="506" stroke="var(--ink)" stroke-width="4"/>
    <text class="date" x="128" y="590">4TH JULY 2021</text>
    <line class="rule" x1="130" y1="604" x2="572" y2="604" stroke="var(--ink)" stroke-width="4"/>

    <!-- program -->
    <text class="program-name" text-anchor="middle">
      <tspan x="485" y="725">LITTLE LUNGS</tspan>
      <tspan x="485" y="752">PROGRAM</tspan>
    </text>
  </svg>
</div>
</body>
</html>
```